Artisan Food and Beverage company needs label for various product

We are an artisan food and beverage company with a range of different snacks, and beverages, such as chips, cold brew coffee and spreads. Because of this, we have different types of packaging - jars, pouches, bottles.
We are looking for a general label design for our different product ranges. We want to have a design that is adaptable to our different packaging containers but that will also distinguish each product from each other. Eg. Different colors for each product range
Our idea is to have the same general look for all but change the color of the border or sides(?) for each product range, We are thinking of something like this:
1. Border: different color per product range (see the collage pic and the screenshot taken from the Pixel Harbor website)
2. Product Category: Eg. Ice Cold Brew , Cheese Dips
- Same size font and type even if one is a pouch and 1 is a flask
3. Product Flavour: Eg. Mocha Latte, Cheddar and Garlic Dip
- Same size font and type even if different packaging (smaler size font
than the product category name
We have added sample pictures of a store label that fits different containers (collage pic) , as well as sample pics of our different packaging containers. We will also have jars for our spreads similar to the jar pic at the top of the collage.
If the design can be editable and the background color (or side color like the one we took a screenshot of here in the website of the crunchy sauce label - pardon that the drop down menu was taken), that is what we have in mind. We should also be able to edit the size so the best pf the whole label so maybe a rectangular label is best.
The "Chef Tobin's" is our official logo.
*Credits to the artist of the Pixel Harbor sample labels we took a screenshot of from the website.

```html
<!DOCTYPE html>
<html lang="en">
<head>
<meta charset="utf-8">
<title>Chef Tobin's Product Labels</title>
<link href="https://fonts.googleapis.com/css2?family=Alegreya+Sans:wght@400;500&display=swap" rel="stylesheet">
<style>
  :root {
    --canvas: #c2c2c2;
    --ink: #231f20;
    --paper: #ffffff;
    --shadow: rgba(0,0,0,0.35);
  }
  html, body {
    margin: 0;
    padding: 0;
    width: 1200px;
    height: 960px;
    overflow: hidden;
    background: var(--canvas);
  }
  .board {
    position: relative;
    width: 1200px;
    height: 960px;
  }
  .label {
    position: absolute;
    display: block;
    border-radius: 5px;
    box-shadow: 4px 5px 6px var(--shadow);
    font-family: "Alegreya Sans", sans-serif;
  }
  .label--wide { width: 278px; height: 209px; }
  .label--square { width: 231px; height: 231px; }
  .category { font-size: 35px; font-weight: 500; fill: var(--ink); }
  .flavour { fill: var(--ink); font-weight: 400; }
  .flavour--wide { font-size: 49px; }
  .flavour--square { font-size: 63px; }
  .brand-name { font-size: 30px; font-weight: 500; fill: var(--ink); }
  .divider { stroke: var(--ink); stroke-width: 3; stroke-linecap: round; }
  .paper { fill: var(--paper); }
  .defs { position: absolute; width: 0; height: 0; }
</style>
</head>
<body>
<svg class="defs" aria-hidden="true">
  <defs>
    <linearGradient id="tone-amber" x1="0" y1="0" x2="0" y2="1">
      <stop offset="0" stop-color="#b57027"/><stop offset="1" stop-color="#d98a36"/>
    </linearGradient>
    <linearGradient id="tone-silver" x1="0" y1="0" x2="0" y2="1">
      <stop offset="0" stop-color="#96979b"/><stop offset="1" stop-color="#c4c5c8"/>
    </linearGradient>
    <linearGradient id="tone-gold" x1="0" y1="0" x2="0" y2="1">
      <stop offset="0" stop-color="#e38d20"/><stop offset="1" stop-color="#f8ca12"/>
    </linearGradient>
    <linearGradient id="tone-mocha" x1="0" y1="0" x2="0" y2="1">
      <stop offset="0" stop-color="#837067"/><stop offset="1" stop-color="#aa938b"/>
    </linearGradient>
  </defs>
</svg>

<main class="board">

  <!-- Amber range -->
  <svg class="label label--wide" style="left:44px;top:170px" viewBox="0 0 500 375">
    <rect width="500" height="375" fill="url(#tone-amber)"/>
    <rect class="paper" y="50" width="500" height="56"/>
    <rect y="53" width="500" height="3" fill="url(#tone-amber)"/>
    <rect y="101" width="500" height="3" fill="url(#tone-amber)"/>
    <rect class="paper" y="333" width="500" height="4"/>
    <rect class="paper" y="343" width="500" height="32"/>
    <path class="paper" d="M152,22 Q250,6 348,22 L348,128 Q250,146 152,128 Z"/>
    <text class="brand-name" x="250" y="86" text-anchor="middle">Chef Tobin's</text>
    <path class="paper" d="M16,165 Q16,155 28,155 L52,155 Q62,145 78,150 Q170,162 250,162 Q330,162 422,150 Q438,145 448,155 L472,155 Q484,155 484,165 L484,318 Q484,325 476,325 L24,325 Q16,325 16,318 Z"/>
    <text class="category" x="250" y="206" text-anchor="middle">CHEESE DIPS</text>
    <line class="divider" x1="183" y1="238" x2="317" y2="238"/>
    <text class="flavour flavour--wide" x="250" y="305" text-anchor="middle">Cheddar and Garlic</text>
  </svg>

  <svg class="label label--square" style="left:336px;top:226px" viewBox="0 0 415 415">
    <rect width="415" height="415" fill="url(#tone-amber)"/>
    <rect class="paper" y="50" width="415" height="56"/>
    <rect y="53" width="415" height="3" fill="url(#tone-amber)"/>
    <rect y="101" width="415" height="3" fill="url(#tone-amber)"/>
    <rect class="paper" y="372" width="415" height="4"/>
    <rect class="paper" y="384" width="415" height="31"/>
    <path class="paper" d="M110,22 Q207,6 305,22 L305,128 Q207,146 110,128 Z"/>
    <text class="brand-name" x="207" y="86" text-anchor="middle">Chef Tobin's</text>
    <path class="paper" d="M17,165 Q17,155 29,155 L48,155 Q58,145 74,150 Q150,162 207,162 Q265,162 340,150 Q356,145 366,155 L386,155 Q398,155 398,165 L398,357 Q398,365 390,365 L25,365 Q17,365 17,357 Z"/>
    <text class="category" x="207" y="218" text-anchor="middle">ICE COLD BREW</text>
    <line class="divider" x1="140" y1="250" x2="274" y2="250"/>
    <text class="flavour flavour--square" x="207" y="321" text-anchor="middle">Mocha Latte</text>
  </svg>

  <!-- Silver range -->
  <svg class="label label--wide" style="left:628px;top:170px" viewBox="0 0 500 375">
    <rect width="500" height="375" fill="url(#tone-silver)"/>
    <rect class="paper" y="50" width="500" height="56"/>
    <rect y="53" width="500" height="3" fill="url(#tone-silver)"/>
    <rect y="101" width="500" height="3" fill="url(#tone-silver)"/>
    <rect class="paper" y="333" width="500" height="4"/>
    <rect class="paper" y="343" width="500" height="32"/>
    <path class="paper" d="M152,22 Q250,6 348,22 L348,128 Q250,146 152,128 Z"/>
    <text class="brand-name" x="250" y="86" text-anchor="middle">Chef Tobin's</text>
    <path class="paper" d="M16,165 Q16,155 28,155 L52,155 Q62,145 78,150 Q170,162 250,162 Q330,162 422,150 Q438,145 448,155 L472,155 Q484,155 484,165 L484,318 Q484,325 476,325 L24,325 Q16,325 16,318 Z"/>
    <text class="category" x="250" y="206" text-anchor="middle">CHEESE DIPS</text>
    <line class="divider" x1="183" y1="238" x2="317" y2="238"/>
    <text class="flavour flavour--wide" x="250" y="305" text-anchor="middle">Cheddar and Garlic</text>
  </svg>

  <svg class="label label--square" style="left:925px;top:226px" viewBox="0 0 415 415">
    <rect width="415" height="415" fill="url(#tone-silver)"/>
    <rect class="paper" y="50" width="415" height="56"/>
    <rect y="53" width="415" height="3" fill="url(#tone-silver)"/>
    <rect y="101" width="415" height="3" fill="url(#tone-silver)"/>
    <rect class="paper" y="372" width="415" height="4"/>
    <rect class="paper" y="384" width="415" height="31"/>
    <path class="paper" d="M110,22 Q207,6 305,22 L305,128 Q207,146 110,128 Z"/>
    <text class="brand-name" x="207" y="86" text-anchor="middle">Chef Tobin's</text>
    <path class="paper" d="M17,165 Q17,155 29,155 L48,155 Q58,145 74,150 Q150,162 207,162 Q265,162 340,150 Q356,145 366,155 L386,155 Q398,155 398,165 L398,357 Q398,365 390,365 L25,365 Q17,365 17,357 Z"/>
    <text class="category" x="207" y="218" text-anchor="middle">ICE COLD BREW</text>
    <line class="divider" x1="140" y1="250" x2="274" y2="250"/>
    <text class="flavour flavour--square" x="207" y="321" text-anchor="middle">Mocha Latte</text>
  </svg>

  <!-- Gold range -->
  <svg class="label label--wide" style="left:44px;top:508px" viewBox="0 0 500 375">
    <rect width="500" height="375" fill="url(#tone-gold)"/>
    <rect class="paper" y="50" width="500" height="56"/>
    <rect y="53" width="500" height="3" fill="url(#tone-gold)"/>
    <rect y="101" width="500" height="3" fill="url(#tone-gold)"/>
    <rect class="paper" y="333" width="500" height="4"/>
    <rect class="paper" y="343" width="500" height="32"/>
    <path class="paper" d="M152,22 Q250,6 348,22 L348,128 Q250,146 152,128 Z"/>
    <text class="brand-name" x="250" y="86" text-anchor="middle">Chef Tobin's</text>
    <path class="paper" d="M16,165 Q16,155 28,155 L52,155 Q62,145 78,150 Q170,162 250,162 Q330,162 422,150 Q438,145 448,155 L472,155 Q484,155 484,165 L484,318 Q484,325 476,325 L24,325 Q16,325 16,318 Z"/>
    <text class="category" x="250" y="206" text-anchor="middle">CHEESE DIPS</text>
    <line class="divider" x1="183" y1="238" x2="317" y2="238"/>
    <text class="flavour flavour--wide" x="250" y="305" text-anchor="middle">Cheddar and Garlic</text>
  </svg>

  <svg class="label label--square" style="left:336px;top:559px" viewBox="0 0 415 415">
    <rect width="415" height="415" fill="url(#tone-gold)"/>
    <rect class="paper" y="50" width="415" height="56"/>
    <rect y="53" width="415" height="3" fill="url(#tone-gold)"/>
    <rect y="101" width="415" height="3" fill="url(#tone-gold)"/>
    <rect class="paper" y="372" width="415" height="4"/>
    <rect class="paper" y="384" width="415" height="31"/>
    <path class="paper" d="M110,22 Q207,6 305,22 L305,128 Q207,146 110,128 Z"/>
    <text class="brand-name" x="207" y="86" text-anchor="middle">Chef Tobin's</text>
    <path class="paper" d="M17,165 Q17,155 29,155 L48,155 Q58,145 74,150 Q150,162 207,162 Q265,162 340,150 Q356,145 366,155 L386,155 Q398,155 398,165 L398,357 Q398,365 390,365 L25,365 Q17,365 17,357 Z"/>
    <text class="category" x="207" y="218" text-anchor="middle">ICE COLD BREW</text>
    <line class="divider" x1="140" y1="250" x2="274" y2="250"/>
    <text class="flavour flavour--square" x="207" y="321" text-anchor="middle">Mocha Latte</text>
  </svg>

  <!-- Mocha range -->
  <svg class="label label--wide" style="left:628px;top:508px" viewBox="0 0 500 375">
    <rect width="500" height="375" fill="url(#tone-mocha)"/>
    <rect class="paper" y="50" width="500" height="56"/>
    <rect y="53" width="500" height="3" fill="url(#tone-mocha)"/>
    <rect y="101" width="500" height="3" fill="url(#tone-mocha)"/>
    <rect class="paper" y="333" width="500" height="4"/>
    <rect class="paper" y="343" width="500" height="32"/>
    <path class="paper" d="M152,22 Q250,6 348,22 L348,128 Q250,146 152,128 Z"/>
    <text class="brand-name" x="250" y="86" text-anchor="middle">Chef Tobin's</text>
    <path class="paper" d="M16,165 Q16,155 28,155 L52,155 Q62,145 78,150 Q170,162 250,162 Q330,162 422,150 Q438,145 448,155 L472,155 Q484,155 484,165 L484,318 Q484,325 476,325 L24,325 Q16,325 16,318 Z"/>
    <text class="category" x="250" y="206" text-anchor="middle">CHEESE DIPS</text>
    <line class="divider" x1="183" y1="238" x2="317" y2="238"/>
    <text class="flavour flavour--wide" x="250" y="305" text-anchor="middle">Cheddar and Garlic</text>
  </svg>

  <svg class="label label--square" style="left:925px;top:559px" viewBox="0 0 415 415">
    <rect width="415" height="415" fill="url(#tone-mocha)"/>
    <rect class="paper" y="50" width="415" height="56"/>
    <rect y="53" width="415" height="3" fill="url(#tone-mocha)"/>
    <rect y="101" width="415" height="3" fill="url(#tone-mocha)"/>
    <rect class="paper" y="372" width="415" height="4"/>
    <rect class="paper" y="384" width="415" height="31"/>
    <path class="paper" d="M110,22 Q207,6 305,22 L305,128 Q207,146 110,128 Z"/>
    <text class="brand-name" x="207" y="86" text-anchor="middle">Chef Tobin's</text>
    <path class="paper" d="M17,165 Q17,155 29,155 L48,155 Q58,145 74,150 Q150,162 207,162 Q265,162 340,150 Q356,145 366,155 L386,155 Q398,155 398,165 L398,357 Q398,365 390,365 L25,365 Q17,365 17,357 Z"/>
    <text class="category" x="207" y="218" text-anchor="middle">ICE COLD BREW</text>
    <line class="divider" x1="140" y1="250" x2="274" y2="250"/>
    <text class="flavour flavour--square" x="207" y="321" text-anchor="middle">Mocha Latte</text>
  </svg>

</main>
</body>
</html>
```